Design Website Templates for Photographers for Lumora Inc. (trywendle.com)

Lumora Inc. is a generative website company for wedding photographers.
We are seeking new photography website design inspirations for the next template to be offered on our platform. The catch is you must use the same data for your designs. You also must use all of the data somewhere in the design. You cannot add new content besides the data available. If you wish to add any elements It will be hardcoded and must be universally fitting for many different photographers. We recommend not using any hardcoded test.
Don't be afraid to be creative! Although the most important element of a photographers website is the photos, we are looking for unique and out-of-the-box designs for the actual site as well.
Here is the User generated data available to you:
- 4 Hero Images Landscape, 4 Hero Images Portrait
- Tagline “destination photographer based in Maui, Hawaii”
- “About Photo” of the photographer
- “About” Biography Text
- The design can use up to 3 colors + background color and 2 fonts
- 9 Gallery images
- 3 Packages/services that include landscape/portrait images, a price, a title and text
- Testimonials made up of an image, text and text for the name of testimonial giver
See some examples of our current website designs attached. You can use any of the data you see in the designs.
Updates
We are looking for designs that are less feminine and are more neutral in color and fonts. Currently our templates are more oriented towards feminine photographers. We want to have designs that speak to diverse audiences. We thank everyone for submitting and are reviewing the designs.
Number of Pages Required
1 page
Look and feel
Each slider illustrates characteristics of the customer's brand and the style your logo design should communicate.

```html
<!DOCTYPE html>
<html lang="en">
<head>
<meta charset="utf-8">
<title>Lumora – Destination Photographer</title>
<link href="https://fonts.googleapis.com/css2?family=Open+Sans:ital,wght@0,400;0,600;0,700;1,400&display=swap" rel="stylesheet">
<style>
:root{
  --ink:#2b2b2b;
  --text:#444;
  --accent:#f2b53a;
  --soft:#f7f7f7;
  --cream:#fde9c4;
  --dark:#222222;
  --white:#ffffff;
  --quote:#e6e6e6;
}
*{margin:0;padding:0;box-sizing:border-box}
html,body{width:1200px;height:4380px;overflow:hidden}
body{font-family:"Open Sans",Arial,sans-serif;color:var(--text);background:var(--white);position:relative}
.abs{position:absolute}
.photo{position:absolute}
.btn{position:absolute;background:var(--accent);color:var(--white);font-size:15px;font-weight:600;display:flex;align-items:center;justify-content:center}
.brand{font-weight:600;font-size:38px;letter-spacing:1px;color:var(--ink);display:flex;align-items:center;gap:10px}
.brand-dot{width:14px;height:14px;border-radius:50%;background:var(--accent)}

/* header + hero */
.hero-band{left:0;top:0;width:1200px;height:514px;background:var(--soft)}
.site-nav{top:38px;left:488px;display:flex;gap:36px;font-size:15px;color:var(--ink)}
.hero-title{left:110px;top:208px;font-size:48px;font-weight:600;line-height:58px;color:var(--ink)}
.hero-title span{color:var(--accent)}
.hero-photo{left:617px;top:110px;width:583px;height:404px;background:linear-gradient(135deg,#3a3836,#8a8683 45%,#d9d5d0 70%,#2a2826)}
.slide-arrow{position:absolute;left:1132px;width:34px;height:34px}

/* about us */
.frame{left:272px;top:609px;width:199px;height:411px;border:2px solid var(--accent)}
.about-main{left:126px;top:593px;width:324px;height:408px;background:linear-gradient(160deg,#2b2418,#6b5536 55%,#c9b79a);box-shadow:0 4px 16px rgba(0,0,0,.15)}
.about-small{left:49px;top:828px;width:220px;height:248px;background:linear-gradient(140deg,#e8e4de,#b9b3aa 60%,#4a5a3e);box-shadow:0 4px 16px rgba(0,0,0,.15)}
.section-title{font-size:43px;font-weight:600;color:var(--ink);letter-spacing:.5px}
.body-copy{font-size:16px;line-height:28px;color:var(--text)}

/* gallery */
.gallery-band{left:0;top:1117px;width:1200px;height:1113px;background:var(--soft)}
.center{left:0;width:1200px;text-align:center}

/* services */
.services-band{left:0;top:3000px;width:1200px;height:669px;background:var(--soft)}
.service{position:absolute;top:3150px;width:292px;text-align:center}
.service .photo{position:relative;width:292px;height:299px}
.service h3{font-size:17px;font-weight:600;color:var(--ink);margin-top:32px}
.service .price{font-size:21px;color:var(--accent);margin-top:4px}
.service p{font-size:15px;line-height:29px;margin-top:2px}

/* testimonials */
.avatar{left:479px;top:3796px;width:102px;height:102px;border-radius:50%;background:linear-gradient(160deg,#a9d8e2,#e8d5c4)}
.quote-mark{font-size:190px;line-height:1;color:var(--quote);font-family:Georgia,serif}
.quote-text{left:192px;top:3918px;width:816px;text-align:center;font-style:italic;font-size:19px;line-height:30px;color:var(--text)}
.dot{position:absolute;top:4076px;width:24px;height:4px;border-radius:2px;background:#d8d8d8}

/* footer */
.site-footer{left:0;top:4136px;width:1200px;height:244px;background:var(--dark);color:var(--white);text-align:center}
.footer-nav{display:flex;justify-content:center;gap:36px;font-size:15px}
</style>
</head>
<body>

<!-- Header + hero -->
<div class="abs hero-band"></div>
<div class="abs brand" style="left:110px;top:26px">LUMORA</div>
<nav class="abs site-nav"><span>Home</span><span>About Us</span><span>Gallery</span><span>Services</span><span>Testimonials</span></nav>
<div class="btn" style="left:981px;top:31px;width:105px;height:40px">Contact Us</div>
<h1 class="abs hero-title">Destination<br>photographer based<br>in <span>Maui, Hawaii</span></h1>
<div class="photo hero-photo" role="img" aria-label="Bride and groom celebrating their exit as guests throw confetti"></div>
<svg class="slide-arrow" style="top:272px" viewBox="0 0 34 34"><circle cx="17" cy="17" r="15" fill="none" stroke="#fff" stroke-width="2"/><path d="M14 10l7 7-7 7" fill="none" stroke="#fff" stroke-width="2"/></svg>
<svg class="slide-arrow" style="top:320px;opacity:.6" viewBox="0 0 34 34"><circle cx="17" cy="17" r="15" fill="none" stroke="#fff" stroke-width="2"/><path d="M20 10l-7 7 7 7" fill="none" stroke="#fff" stroke-width="2"/></svg>

<!-- About us -->
<div class="abs frame"></div>
<div class="photo about-main" role="img" aria-label="Couple embracing under warm evening string lights"></div>
<div class="photo about-small" role="img" aria-label="Hands exchanging a wedding ring over a bouquet"></div>
<h2 class="abs section-title" style="left:590px;top:644px">ABOUT US</h2>
<p class="abs body-copy" style="left:590px;top:722px;width:500px">Lorem ipsum dolor sit amet, consectetur adipiscing elit, sed do eiusmod tempor incididunt ut labore et dolore magna aliqua. Ut enim ad minim veniam, quis nostrud exercitation ullamco laboris nisi ut aliquip ex ea commodo consequat. Duis aute irure dolor in reprehenderit in voluptate velit esse cillum dolore eu fugiat nulla pariatur. Excepteur sint occaecat cupidatat non proident, sunt in culpa qui officia deserunt mollit anim id est laborum.</p>
<div class="btn" style="left:590px;top:954px;width:107px;height:40px">Contact Us</div>

<!-- Gallery -->
<div class="abs gallery-band"></div>
<h2 class="abs section-title center" style="top:1166px">OUR GALLERY</h2>
<p class="abs body-copy" style="left:170px;top:1236px;width:860px;text-align:center">Lorem ipsum dolor sit amet, consectetur adipiscing elit, sed do eiusmod tempor incididunt ut labore et dolore magna aliqua. Ut enim ad minim veniam, quis nostrud exercitation ullamco laboris nisi ut aliquip ex ea commodo consequat.</p>

<div class="photo" style="left:112px;top:1346px;width:308px;height:279px;background:linear-gradient(135deg,#d9c08c,#a88a5a 50%,#3a4150)" role="img" aria-label="Couple in a golden field"></div>
<div class="photo" style="left:112px;top:1651px;width:308px;height:280px;background:linear-gradient(135deg,#3a3a3a,#c9a8a8 55%,#ece6e2)" role="img" aria-label="Hands holding a dusty rose bouquet"></div>
<div class="photo" style="left:112px;top:1952px;width:308px;height:440px;background:linear-gradient(180deg,#5a6a3a,#d8d2c6 45%,#8a7a4a)" role="img" aria-label="Floral ceremony arch in a forest"></div>

<div class="photo" style="left:459px;top:1346px;width:367px;height:354px;background:linear-gradient(135deg,#f2f0ec,#e3d8cc 50%,#d9c9a8)" role="img" aria-label="Hands with wedding rings over white roses"></div>
<div class="photo" style="left:459px;top:1726px;width:367px;height:353px;background:linear-gradient(135deg,#2a1a0c,#b77a30 50%,#3a2512)" role="img" aria-label="Couple framed by glowing lights in a doorway"></div>
<div class="photo" style="left:459px;top:2103px;width:367px;height:289px;background:linear-gradient(160deg,#1e2a1a,#4a5a32 50%,#c8b89a)" role="img" aria-label="Couple walking under string lights at night"></div>

<div class="photo" style="left:864px;top:1346px;width:226px;height:279px;background:linear-gradient(135deg,#dfe4e2,#b6bcb6 55%,#4a4a48)" role="img" aria-label="Couple kissing in a misty garden"></div>
<div class="photo" style="left:864px;top:1651px;width:226px;height:280px;background:linear-gradient(135deg,#eeeae4,#c7bfb6 55%,#9c8f86)" role="img" aria-label="Two wedding rings on glitter"></div>
<div class="photo" style="left:864px;top:1952px;width:226px;height:440px;background:linear-gradient(180deg,#f4eedc,#d8cdb4 45%,#8a7a62)" role="img" aria-label="Couple embracing in a meadow"></div>

<!-- About me -->
<h2 class="abs section-title" style="left:112px;top:2540px">ABOUT ME</h2>
<p class="abs body-copy" style="left:112px;top:2618px;width:500px">Lorem ipsum dolor sit amet, consectetur adipiscing elit, sed do eius mod tempor incididunt ut labore et dolore magna aliqua. Ut enim ad minim veniam, quis nostrud exercitation ullamco laboris nisi ut aliquip ex ea commodo consequat. Duis aute irure dolor in reprehenderit in voluptate velit esse cillum dolore eu fugiat nulla pariatur. Excepteur sint occaecat cupidatat non proident, sunt in culpa qui officia deserunt mollit anim id est laborum.</p>
<div class="btn" style="left:112px;top:2849px;width:106px;height:41px">Contact Us</div>
<div class="abs" style="left:762px;top:2506px;width:438px;height:408px;background:var(--cream)"></div>
<div class="photo" style="left:741px;top:2489px;width:327px;height:408px;background:linear-gradient(160deg,#f0f0f0,#bdbdbd 55%,#2c2c2c);box-shadow:0 4px 16px rgba(0,0,0,.18)" role="img" aria-label="Photographer with a camera in a studio"></div>

<!-- Services -->
<div class="abs services-band"></div>
<h2 class="abs section-title center" style="top:3052px">OUR SERVICES</h2>
<div class="service" style="left:112px">
  <div class="photo" style="background:linear-gradient(180deg,#e6e2da,#a89a7a 50%,#5a4a36)" role="img" aria-label="Couple under a floral wooden pavilion"></div>
  <h3>LOREM IPSUM</h3><div class="price">$105</div><p>Lorem ipsum dolor sit amet, con sectetur adipiscing elit.</p>
</div>
<div class="service" style="left:455px">
  <div class="photo" style="background:linear-gradient(180deg,#f3f1ec,#d6d0c4 55%,#8a9a6a)" role="img" aria-label="White draped ceremony setup with flowers"></div>
  <h3>LOREM IPSUM</h3><div class="price">$105</div><p>Lorem ipsum dolor sit amet, con sectetur adipiscing elit.</p>
</div>
<div class="service" style="left:798px">
  <div class="photo" style="background:linear-gradient(160deg,#3a2a1a,#1a1a1a 50%,#6a6460)" role="img" aria-label="Couple dancing at night under a lantern"></div>
  <h3>LOREM IPSUM</h3><div class="price">$105</div><p>Lorem ipsum dolor sit amet, con sectetur adipiscing elit.</p>
</div>

<!-- Testimonials -->
<h2 class="abs section-title center" style="top:3722px">TESTIMONIALS</h2>
<div class="abs avatar" role="img" aria-label="Portrait of the client"></div>
<div class="abs" style="left:602px;top:3822px;font-size:18px;color:var(--ink)">MAREN T.</div>
<svg class="abs" style="left:600px;top:3853px" width="122" height="22" viewBox="0 0 122 22">
  <g fill="#f2b53a">
    <path id="st" d="M10 1l2.6 6.4 6.9.5-5.3 4.4 1.7 6.7L10 15.3 4.1 19l1.7-6.7L.5 7.9l6.9-.5z"/>
    <use href="#st" x="25"/><use href="#st" x="50"/><use href="#st" x="75"/><use href="#st" x="100"/>
  </g>
</svg>
<div class="abs quote-mark" style="left:108px;top:3818px">&ldquo;</div>
<div class="abs quote-mark" style="left:996px;top:4027px">&rdquo;</div>
<p class="abs quote-text">Sed ut perspiciatis unde omnis iste natus error sit voluptatem accusantium doloremque laudantium, totam rem aperiam, eaque ipsa quae ab illo inventore veritatis et quasi architecto beatae vitae dicta sunt explicabo. Nemo enim ipsam voluptatem quia voluptas sit aspernatur aut odit aut fugit</p>
<div class="dot" style="left:547px"></div>
<div class="dot" style="left:588px;background:var(--accent)"></div>
<div class="dot" style="left:627px"></div>

<!-- Footer -->
<footer class="abs site-footer">
  <div class="brand" style="color:var(--white);justify-content:center;margin-top:50px">LUMORA</div>
  <nav class="footer-nav" style="margin-top:18px"><span>Home</span><span>About Us</span><span>Gallery</span><span>Services</span><span>Testimonials</span></nav>
  <div style="font-size:15px;margin-top:14px">2023 Lumora. All Rights Reserved.</div>
</footer>

</body>
</html>
```